Jewelry Shop Needs a Business Card Design

***We want a very sharp and unforgettable pantone for the Business Card. ***
***We do not want the business card or logo only in black, white and grey color!!!Please provide us a main color as our brand topic! Thanks!! ***

Mabel’s Nook is a Hong Kong based fine jewelry brand.

We want a very nice, simple and elegant business card design for Mabel's Nook Brand. The company's logo has been uploaded already.

You can design with below info:

Dorian Fung
Director
M: +852 94273658
T: +852 35820417
F: +852 35820419
E: dorian.fung@mabelsnook.example
5/F , Harbourlight Tower, 12-18 Orchid Lane, Wan Tung Kok, Kowloon, Hong Kong

Target Market(s)

Mabel’s Nook philosophy is a jewelry icon of young, creative, trendy, fashionable, stylish, energetic, and elegant. For Mabel’s Nook, jewelry is one collection of artworks, the most important items in personal life.

Industry/Entity Type

Jewelry

Requirements
Must have
• We want a very sharp and unforgettable pantone for the Business Card.

```html
<!DOCTYPE html>
<html lang="en">
<head>
<meta charset="utf-8">
<title>Mabel's Nook – Business Card</title>
<link rel="stylesheet" href="https://fonts.googleapis.com/css2?family=Tinos:ital,wght@0,400;0,700;1,400;1,700&display=swap">
<style>
  :root {
    --paper: #ffffff;
    --plum: #4a0426;
    --plum-light: #9a5a78;
    --rose-band: #c53c64;
    --ink: #0a0006;
    --mauve-text: #85506c;
    --mauve-soft: #7a4463;
    --logo-disc: #8c5f76;
    --logo-ring: #b592a5;
    --tagline: #f3a6c8;
    --rule: #1a0a12;
  }
  * { box-sizing: border-box; margin: 0; padding: 0; }
  html, body {
    width: 848px; height: 1200px; overflow: hidden;
    background: var(--paper);
  }
  body {
    position: relative;
    font-family: "Tinos", "Times New Roman", serif;
  }
  .card {
    position: absolute;
    left: 241px;
    width: 357px;
    height: 204px;
    background: var(--paper);
    overflow: hidden;
  }
  .card--front { top: 270px; }
  .card--back { top: 663px; }

  .card__field {
    position: absolute; left: 0; top: 0; width: 100%;
    background: var(--plum);
  }
  .card--front .card__field { height: 169px; }
  .card--back .card__field {
    height: 165px;
    background:
      radial-gradient(ellipse 62% 70% at 50% 55%, rgba(190,120,150,0.75) 0%, rgba(140,70,105,0.55) 40%, rgba(74,4,38,0) 100%),
      var(--plum);
  }
  .card__rule {
    position: absolute; left: 0; width: 100%; height: 2px;
    background: var(--rule);
  }
  .card__band {
    position: absolute; left: 0; bottom: 0; width: 100%;
    background: var(--rose-band);
    color: var(--ink);
    font-style: italic;
    text-align: center;
  }
  .card--front .card__band { height: 28px; font-size: 13px; line-height: 28px; }
  .card--back .card__band { height: 30px; font-size: 12px; line-height: 15px; padding-top: 1px; }

  .brand-mark {
    position: absolute; left: 4px; top: 9px; width: 112px;
    text-align: center;
  }
  .brand-mark__disc {
    display: block; margin: 0 auto;
  }
  .brand-mark__name {
    display: block; margin-top: 4px;
    font-size: 11px; font-weight: 700;
    color: var(--logo-ring);
    letter-spacing: 0.3px;
  }

  .person {
    position: absolute; left: 130px; top: 74px; width: 110px;
    text-align: center; font-style: italic;
  }
  .person__name { font-size: 20px; color: var(--mauve-text); line-height: 24px; }
  .person__role { font-size: 14px; color: var(--mauve-text); line-height: 16px; margin-left: -8px; }

  .contacts {
    position: absolute; right: 8px; top: 9px;
    list-style: none; text-align: right;
    font-style: italic; font-size: 12px; line-height: 17.5px;
    color: var(--mauve-soft);
  }

  .wordmark {
    position: absolute; left: 0; top: 66px; width: 100%;
    text-align: center;
    font-size: 34px; line-height: 38px;
    color: var(--logo-ring);
    letter-spacing: 0.5px;
  }
  .tagline {
    position: absolute; left: 0; top: 110px; width: 100%;
    text-align: center;
    font-size: 12px; font-style: italic; font-weight: 700;
    color: var(--tagline);
  }
</style>
</head>
<body>

  <section class="card card--front" aria-label="Business card front">
    <div class="card__field"></div>

    <div class="brand-mark">
      <svg class="brand-mark__disc" width="58" height="58" viewBox="0 0 58 58" aria-hidden="true">
        <circle cx="29" cy="29" r="28" fill="var(--logo-disc)" stroke="var(--logo-ring)" stroke-width="1"/>
      </svg>
      <span class="brand-mark__name">Mabel's Nook</span>
    </div>

    <div class="person">
      <p class="person__name">Dorian Fung</p>
      <p class="person__role">Director</p>
    </div>

    <ul class="contacts">
      <li>M: +852 94273658</li>
      <li>T: +852 35820417</li>
      <li>F: +852 35820419</li>
    </ul>

    <div class="card__rule" style="top:170px"></div>
    <div class="card__rule" style="top:174px"></div>
    <p class="card__band">dorian.fung@mabelsnook.example</p>
  </section>

  <section class="card card--back" aria-label="Business card back">
    <div class="card__field"></div>
    <p class="wordmark">Mabel's Nook</p>
    <p class="tagline">We bring you the most beautiful jewelry!</p>

    <div class="card__rule" style="top:166px"></div>
    <div class="card__rule" style="top:170px"></div>
    <p class="card__band">5/F, Harbourlight Tower 12-18 Orchid Lane,<br>Wan Tung Kok, Kowloon, Hong Kong</p>
  </section>

</body>
</html>
```